Orbell Consulting- executive coaching business

looking for business card design for a newly started coaching business.
specialising in Exective coaching, Leadership, NLP and Motivation.
Looking for a simple, classy design using the existing logo attached and colour themes that complement the logo.
No red or orange in the business card design please.

Target Market(s)

Defence and Veteran community

Industry/Entity Type

Life Coaching

Contact Information for Business Card

looking for business cards for newly started coaching business.
specialising in Exective Coaching, Leadership, NLP and Motivation

Font styles to use
Serif
Script

Colors
0556a4
3176b5
86cfc6
33b8a4

Requirements
Must have
• Logo
• Email address- Jess@orbellconsulting.com.au
• Contact number
• Services provided - Executive Coaching, Leadership, NLP and Motivational Mapping.
Nice to have
• Same colours as logo
Should not have
• Red or orange

```html
<!DOCTYPE html>
<html lang="en">
<head>
<meta charset="utf-8">
<title>Orbell Consulting – Business Cards</title>
<link rel="stylesheet" href="https://fonts.googleapis.com/css2?family=Open+Sans:ital,wght@0,400;0,600;0,700;1,700&display=swap">
<style>
  :root {
    --bg: #ecebe9;
    --card: #ffffff;
    --blue: #1d5fae;
    --blue-deep: #0556a4;
    --green: #3ba54a;
    --grey: #8c8c8c;
    --ink: #555555;
  }
  * { box-sizing: border-box; margin: 0; padding: 0; }
  html, body { width: 1200px; height: 799px; overflow: hidden; }
  body {
    background: var(--bg);
    font-family: "Open Sans", Arial, sans-serif;
    position: relative;
  }
  .card {
    position: absolute;
    top: 250px;
    width: 520px;
    height: 298px;
    background: var(--card);
    box-shadow: 0 6px 18px rgba(0,0,0,0.12);
    overflow: hidden;
    text-align: center;
  }
  .card--contact { left: 50px; }
  .card--services { left: 630px; }

  .corner {
    position: absolute;
    width: 120px;
    height: 120px;
    border-radius: 50%;
    background: radial-gradient(circle at 40% 40%, var(--blue) 0%, var(--blue-deep) 100%);
  }
  .corner--top-left { top: -60px; left: -60px; }
  .corner--bottom-right { bottom: -60px; right: -60px; }

  .brand {
    display: inline-flex;
    align-items: center;
    gap: 10px;
  }
  .brand__name {
    font-weight: 700;
    font-size: 26px;
    color: var(--blue);
    letter-spacing: 0.5px;
  }
  .brand__dot { width: 34px; height: 34px; }

  .rule {
    width: 200px;
    height: 2px;
    background: var(--green);
    margin: 8px auto 0;
  }

  .card--contact .person { margin-top: 62px; }
  .person__name { font-weight: 700; font-size: 17px; color: var(--blue); }
  .person__title { font-size: 11px; color: var(--ink); }
  .card--contact .brand { margin-top: 10px; }

  .details { margin-top: 14px; font-size: 11px; color: var(--ink); line-height: 1.55; }
  .details__web { font-weight: 700; color: var(--blue); font-size: 12px; }

  .card--services .brand { margin-top: 84px; }
  .services__label { margin-top: 10px; font-weight: 700; font-style: italic; font-size: 12px; color: var(--blue); }
  .services__list { margin-top: 2px; font-weight: 700; font-style: italic; font-size: 12.5px; color: var(--blue); }
  .services__web { margin-top: 4px; font-size: 11.5px; color: var(--green); }
</style>
</head>
<body>
  <section class="card card--contact">
    <span class="corner corner--top-left"></span>
    <span class="corner corner--bottom-right"></span>
    <div class="person">
      <p class="person__name">Dana Whitfield</p>
      <p class="person__title">President</p>
    </div>
    <div class="brand">
      <span class="brand__name">Orbell Consulting</span>
      <svg class="brand__dot" viewBox="0 0 34 34" aria-hidden="true"><circle cx="17" cy="17" r="15" fill="none" stroke="#8c8c8c" stroke-width="2"/></svg>
    </div>
    <div class="rule"></div>
    <div class="details">
      <p>#48, Harbour Lane, Newtown, Australia</p>
      <p>P: 02.9123.4567, C: 0412.345.678, F: 02.9123.4568, E: jess@orbellconsulting.com.au</p>
      <p class="details__web">www.orbellconsulting.com.au</p>
    </div>
  </section>

  <section class="card card--services">
    <div class="brand">
      <span class="brand__name">Orbell Consulting</span>
      <svg class="brand__dot" viewBox="0 0 34 34" aria-hidden="true"><circle cx="17" cy="17" r="15" fill="none" stroke="#8c8c8c" stroke-width="2"/></svg>
    </div>
    <div class="rule"></div>
    <p class="services__label">- Services provided -</p>
    <p class="services__list">Executive Coaching, Leadership, NLP and Motivational Mapping.</p>
    <p class="services__web">www.orbellconsulting.com.au</p>
  </section>
</body>
</html>
```